High Profile Web Design Project

We need a sleek,state-of-the-art design for an international real estate company based in the Gulf region.

Fonts should be modern and clean, and a corner should in the top banner should be reserved for the logo.

The logo of the company is gold, navy blue, and white so the website should coincide with this.

The site will actually be an internal portal so it is important that the focus is on content.

This is the first of many requests. Top ten designers will be contacted repeatedly both via the site and privately for further business.

As this is an internal portal for employees, focus should be on news, policies, search, complaints, etc.

Hi All, 

More information on the requirements: 

1- Group Homepage (Do not include department  component like : Department News, Department Blog, Poll, Calendar)

·         Company Announcements

·         Velmora in Press

·         Highlights / Achievements (Three main blocks with photos )

·         Photo Gallery

·         Quick Links (Trackon – Ledgrix – Organization Structure – Phone Directory …)

·         Navigation tabs
- Properties (Include sub links for departments)
-International (Include sub links for countries list)
-  Hospitality (Include sub links for hotels)
- Retail (Include sub links for attractions)
- Malls Group (Include sub links for malls)
- Technologies

 

2-      Department Homepage (Information technology for example but can be applied for Finance, HR, Marketing, Mall, Hotel…etc)

·         Department Announcements

·         Technology News

·         Project Office

·         Quick Links (Trackon – Ledgrix – IT Policies – Activity Calendar …)

·         Department Blog

·         Poll (Best Project – Employee of the month – Best Photography)... one poll  at time

 

Target Market(s)

real-estate employees

Industry/Entity Type

Real Estate

Requirements
Must have
• - Space in the corner for the logo (which is a square logo);
- Colors which match with navy blue & gold;
- Content centric design;
Should not have
• Scrolling - we want to try to limit the need for scrolling - especially on the portal home page.

```html
<!DOCTYPE html>
<html lang="en">
<head>
<meta charset="utf-8">
<title>Velmora Portal</title>
<link rel="stylesheet" href="https://fonts.googleapis.com/css2?family=Questrial&family=Arimo:ital,wght@0,400;0,700;1,400;1,700&display=swap">
<style>
  :root {
    --header-bg: #17191c;
    --header-rule: #3b3e42;
    --page-bg: #111419;
    --card-bg: #161a1f;
    --footer-bg: #0e1013;
    --text-light: #f2f2f2;
    --text-muted: #8b8e92;
    --footer-link: #b9bcc0;
    --accent-green: #22b52a;
    --logo-gold: #f0c060;
    --field-border: #c9c9c9;
    --divider: #5a5d61;
  }
  * { margin: 0; padding: 0; box-sizing: border-box; }
  html, body { width: 1200px; height: 949px; overflow: hidden; background: var(--page-bg); }
  body { position: relative; font-family: "Questrial", sans-serif; color: var(--text-light); }

  .site-header { position: absolute; left: 0; top: 0; width: 1200px; height: 93px; background: var(--header-bg); border-bottom: 5px solid var(--header-rule); }
  .brand { position: absolute; left: 58px; top: 28px; display: flex; align-items: center; gap: 8px; font-size: 24px; color: var(--logo-gold); }
  .brand-mark { width: 14px; height: 14px; background: var(--logo-gold); }
  .main-nav { position: absolute; left: 184px; top: 35px; display: flex; }
  .main-nav a { display: block; height: 24px; line-height: 24px; border-left: 1px solid var(--divider); text-align: center; color: var(--text-light); text-decoration: none; font-size: 22px; }
  .main-nav a:last-child { border-right: 1px solid var(--divider); }

  .hero { position: absolute; left: 0; top: 93px; width: 1200px; height: 409px; }
  .hero-scene { position: absolute; inset: 0;
    background:
      linear-gradient(180deg, rgba(0,0,0,0) 45%, rgba(60,78,22,0.85) 75%, rgba(38,48,16,0.95) 100%),
      linear-gradient(100deg, #15200e 0%, #2c3d15 28%, #6a5a1a 45%, #d08a1a 62%, #f3b420 85%, #e39a1a 100%); }
  .newsletter { position: absolute; left: 121px; top: 190px; width: 220px; }
  .newsletter h2 { font-family: "Arimo", sans-serif; font-weight: 700; font-size: 16px; margin: 0 0 10px 2px; }
  .field { display: block; width: 215px; height: 44px; border: 2px solid var(--field-border); border-radius: 8px; background: rgba(255,255,255,0.08); color: var(--field-border); font-family: "Arimo", sans-serif; font-style: italic; font-weight: 700; font-size: 16px; line-height: 40px; padding-left: 12px; margin-bottom: 5px; }
  .field + .field { height: 40px; line-height: 36px; }
  .subscribe-btn { display: block; margin: 5px 0 0 42px; width: 126px; height: 42px; border: 2px solid var(--field-border); border-radius: 8px; background: rgba(0,0,0,0.25); color: var(--field-border); font-family: "Arimo", sans-serif; font-style: italic; font-weight: 700; font-size: 16px; text-align: center; line-height: 38px; }
  .tagline { position: absolute; left: 629px; top: 354px; font-family: "Arimo", sans-serif; font-style: italic; font-weight: 700; font-size: 36px; color: #d4d6d8; text-shadow: 1px 2px 3px rgba(0,0,0,0.6); letter-spacing: 0.3px; }

  .content { position: absolute; left: 56px; top: 539px; width: 1060px; height: 253px; }
  .card { position: absolute; top: 0; width: 354px; height: 253px; background: var(--card-bg); padding: 26px 22px 0 27px; }
  .card--plain { background: transparent; }
  .card h3 { font-weight: 400; font-size: 23px; line-height: 26px; padding-bottom: 2px; border-bottom: 1px solid var(--divider); width: 303px; }
  .card p { margin-top: 5px; font-size: 17.5px; line-height: 20px; color: var(--text-muted); width: 320px; white-space: nowrap; }
  .view-more { display: block; width: 303px; text-align: right; margin-top: 3px; font-family: "Arimo", sans-serif; font-style: italic; font-size: 16px; color: var(--accent-green); text-decoration: none; }

  .site-footer { position: absolute; left: 0; top: 879px; width: 1200px; height: 70px; background: var(--footer-bg); }
  .footer-nav a { position: absolute; top: 30px; font-size: 15px; color: var(--footer-link); text-decoration: none; }
  .copyright { position: absolute; left: 785px; top: 27px; font-size: 18px; color: var(--footer-link); }
</style>
</head>
<body>
  <header class="site-header">
    <div class="brand"><span class="brand-mark"></span>Velmora</div>
    <nav class="main-nav">
      <a href="#" style="width:100px">Home</a>
      <a href="#" style="width:138px">News</a>
      <a href="#" style="width:134px">Policies</a>
      <a href="#" style="width:179px">Complaints</a>
      <a href="#" style="width:138px">About Us</a>
      <a href="#" style="width:163px">Contact Us</a>
    </nav>
  </header>

  <section class="hero">
    <div class="hero-scene" role="img" aria-label="Countryside at sunset: trees, a wooden cabin in a meadow, a lake and hills under an orange sky"></div>
    <form class="newsletter">
      <h2>Subscribe to our Newsletter</h2>
      <span class="field">Name</span>
      <span class="field">Name@email.com</span>
      <span class="subscribe-btn">Subscribe</span>
    </form>
    <p class="tagline">Have a pleasant stay with us..</p>
  </section>

  <main class="content">
    <article class="card" style="left:0">
      <h3>About US</h3>
      <p>Lorem ipsum dolor sit amet,<br>consectetuer adipiscing elit, sed<br>diam nonummy nibh euismod<br>tincidunt ut laoreet dolore magna<br>aliquam erat volutpat. Ut wisi enim<br>ad minim veniam, quis nostrud<br>exerci tation ullamcorper suscipit</p>
      <a class="view-more" href="#">[View more]</a>
    </article>
    <article class="card card--plain" style="left:351px">
      <h3>Our New Plans</h3>
      <p>Lorem ipsum dolor sit amet,<br>consectetuer adipiscing elit, sed<br>diam nonummy nibh euismod<br>tincidunt ut laoreet dolore magna<br>aliquam erat volutpat. Ut wisi enim<br>ad minim veniam, quis nostrud<br>exerci tation ullamcorper suscipit</p>
      <a class="view-more" href="#">[View more]</a>
    </article>
    <article class="card" style="left:707px">
      <h3>News</h3>
      <p>Lorem ipsum dolor sit amet,<br>consectetuer adipiscing elit, sed<br>diam nonummy nibh euismod<br>tincidunt ut laoreet dolore magna<br>aliquam erat volutpat. Ut wisi enim<br>ad minim veniam, quis nostrud<br>exerci tation ullamcorper suscipit</p>
      <a class="view-more" href="#">[View more]</a>
    </article>
  </main>

  <footer class="site-footer">
    <nav class="footer-nav">
      <a href="#" style="left:81px">Home</a>
      <a href="#" style="left:166px">News</a>
      <a href="#" style="left:246px">Policies</a>
      <a href="#" style="left:336px">Complaints</a>
      <a href="#" style="left:446px">About Us</a>
      <a href="#" style="left:537px">Contact Us</a>
    </nav>
    <p class="copyright">Copyright@design&nbsp;&nbsp; All right reserved</p>
  </footer>
</body>
</html>
```